Innovative & Professional Website for condo development company
Kelvar Builds Inc.
Innovative & Professional Website for condo development company - Architecture
Creative Brief
Architecture
www.kelvarbuilds-example.com
We are development company who primarily invests in and builds multi-family housing projects. We focus on designing and building attractive, modern, energy-efficient homes. From townhouse developments to condo strata, we specialize in creating extraordinary living spaces. Our company was established with a strong foundation of strategic partnerships, expertise in business and venture capital structure design.
Likes: creativity, clean, innovative design, originality, eye-catching Dislikes: too much clutter or page coverage,
White
Blues
Grays, Black
below header
http://www.layoutgrove-example.com/joomla-templates/40669.html
http://www.layoutgrove-example.com/joomla-templates/38108.html
http://www.layoutgrove-example.com/flash-cms-templates/43354.html
We are open to seeing a variety of your creative designs and are looking for the ability to have a cms login and capabilities. Pages & headings HOME COMPANY: area for company bio, services, markets we operate in, business strategy & development process DEVELOPMENTS: area to list each project description, photos, web links, future projects INSPIRATION: area to display engineering and architectural design that inspires us PARTNERS: area to list each partner with their logo/pic- as well as a 'Partner Login' CONTACT: form, display our email: info@kelvarbuilds-example.com, no phone number Other general things that could be added: facebook & twitter logos embedded with links Condos for sale “We Invest in local tangibility” News feed possibly Thanks!!!

```html
<!DOCTYPE html>
<html lang="en">
<head>
<meta charset="utf-8">
<title>Kelvar Builds Inc. — Building High End Work</title>
<link rel="stylesheet" href="https://fonts.googleapis.com/css2?family=Open+Sans:wght@400;600;700;800&display=swap">
<style>
:root{
  --navy:#1d3a5f;
  --panel:rgba(24,52,88,0.92);
  --panel-line:rgba(255,255,255,0.12);
  --sky-top:#dfe9f3;
  --sky-mid:#9db8d4;
  --sky-low:#4f78a4;
  --accent:#e8792a;
  --ink:#1b1b1b;
  --text:#444;
  --muted:#777;
  --rule:#cfd4da;
  --page:#ffffff;
}
*{margin:0;padding:0;box-sizing:border-box}
html,body{width:1200px;height:1044px;overflow:hidden}
body{background:var(--page);font-family:"Open Sans",Arial,sans-serif;color:var(--text);position:relative}

.site-header{position:absolute;left:0;top:0;width:1200px;height:122px;background:var(--page)}
.brand{position:absolute;left:136px;top:30px;display:flex;align-items:center;gap:10px;white-space:nowrap}
.brand-mark{width:40px;height:40px;background:var(--navy);flex:none}
.brand-name{font-size:24px;font-weight:800;color:var(--navy);letter-spacing:.3px;line-height:1;white-space:nowrap}
.partner-login{position:absolute;left:925px;top:28px;width:133px;height:24px;background:var(--navy);color:#fff;font-size:11px;line-height:24px;text-align:center;border-radius:3px}
.main-nav{position:absolute;left:549px;top:76px;display:flex;gap:6px}
.main-nav a{display:block;height:22px;line-height:22px;padding:0 10px;font-size:12px;font-weight:600;color:var(--navy);text-decoration:none;text-transform:uppercase}
.main-nav a.is-active{background:var(--navy);color:#fff;border-radius:2px}

.hero{position:absolute;left:0;top:122px;width:1200px;height:543px;
  background:linear-gradient(180deg,var(--sky-top) 0%,var(--sky-mid) 45%,var(--sky-low) 100%)}
.hero-copy{position:absolute;left:232px;top:72px}
.hero-title{font-size:38px;font-weight:700;color:var(--ink);letter-spacing:.5px;line-height:1}
.hero-sub{margin-top:18px;font-size:27px;font-weight:600;color:var(--ink);letter-spacing:1px;line-height:1}
.hero-dots{position:absolute;left:240px;top:184px;display:flex;gap:8px}
.hero-dots span{width:22px;height:22px;border-radius:50%;background:#3a3f46}

.features{position:absolute;left:133px;top:552px;width:931px;height:254px;background:var(--panel);border-radius:6px;display:flex}
.feature{flex:1;padding:22px 18px 0;border-right:1px solid var(--panel-line);position:relative;min-width:0}
.feature:last-child{border-right:0}
.feature-head{display:flex;align-items:center;gap:10px;margin-bottom:10px;white-space:nowrap}
.feature-icon{width:28px;height:28px;background:var(--accent);border-radius:3px;display:flex;align-items:center;justify-content:center;flex:none}
.feature-title{font-size:16px;font-weight:700;color:#fff;text-transform:uppercase}
.feature p{font-size:11px;line-height:15px;color:#d7e1ec;margin-bottom:10px}
.feature p.lead{color:#f0b07a}
.read-more{position:absolute;left:18px;top:208px;font-size:12px;font-weight:700;color:#fff;text-transform:uppercase;text-decoration:none}

.site-footer{position:absolute;left:0;top:806px;width:1200px;height:238px}
.footer-col{position:absolute;top:30px}
.footer-col h3{font-size:13px;font-weight:600;color:var(--ink);text-transform:uppercase;padding-bottom:8px;border-bottom:1px solid var(--rule);margin-bottom:12px}
.footer-col ul{list-style:none}
.footer-col li{font-size:11px;line-height:15px;color:var(--text)}
.col-links{left:167px;width:110px}
.col-news{left:317px;width:270px}
.col-news p{font-size:11px;line-height:15px;margin-bottom:2px}
.col-news .date{margin-bottom:14px}
.col-signup{left:634px;width:220px}
.col-signup p{font-size:11px;line-height:15px;margin-bottom:8px}
.signup-input{width:215px;height:22px;border:1px solid var(--rule);font-size:10px;line-height:20px;padding:0 6px;color:var(--muted);background:#fff}
.signup-btn{margin-top:9px;width:70px;height:22px;background:var(--navy);color:#fff;font-size:11px;line-height:22px;text-align:center;border-radius:3px}
.col-contact{left:897px;width:170px}
.contact-brand{margin-top:20px;display:flex;align-items:center;gap:8px;white-space:nowrap}
.contact-brand .brand-mark{width:22px;height:22px;background:#444}
.contact-brand .brand-name{font-size:13px;color:#444;letter-spacing:0}
.footer-rule{position:absolute;left:167px;top:182px;width:897px;border-top:1px solid var(--rule)}
.copyright{position:absolute;left:167px;top:190px;font-size:11px;color:var(--text)}
</style>
</head>
<body>

<header class="site-header">
  <div class="brand">
    <span class="brand-mark"></span>
    <span class="brand-name">KELVAR BUILDS INC.</span>
  </div>
  <div class="partner-login">Partner Login | Signup</div>
  <nav class="main-nav">
    <a class="is-active" href="#">Home</a>
    <a href="#">Our Company</a>
    <a href="#">Development</a>
    <a href="#">Inspiration</a>
    <a href="#">Partners</a>
    <a href="#">Contact Us</a>
  </nav>
</header>

<section class="hero" role="img" aria-label="Upward view of modern glass office towers against a pale blue sky">
  <div class="hero-copy">
    <h1 class="hero-title">BUILDING HIGH END WORK</h1>
    <h2 class="hero-sub">FOR VERY REASONABLE PRICES...</h2>
  </div>
  <div class="hero-dots"><span></span><span></span><span></span></div>
</section>

<section class="features">
  <article class="feature">
    <div class="feature-head">
      <span class="feature-icon"><svg width="14" height="14" viewBox="0 0 14 14"><rect x="2" y="2" width="10" height="10" fill="none" stroke="#fff" stroke-width="2"/></svg></span>
      <span class="feature-title">Introduction</span>
    </div>
    <p class="lead">Lorem ipsum dolor sit amet, consectetur adipiscing elit. Morbi sollicitudin convallis elementum. Nullam cursus condimentum lectus.</p>
    <p>Curabitur at mi a lectus feugiat cursus sed in est. Donec ac ipsum elit, vitae egestas augue.</p>
    <a class="read-more" href="#">Read more...</a>
  </article>
  <article class="feature">
    <div class="feature-head">
      <span class="feature-icon"><svg width="14" height="14" viewBox="0 0 14 14"><circle cx="6" cy="6" r="4" fill="none" stroke="#fff" stroke-width="2"/><path d="M9 9l4 4" stroke="#fff" stroke-width="2"/></svg></span>
      <span class="feature-title">Kelvar Services</span>
    </div>
    <p class="lead">Lorem ipsum dolor sit amet, consectetur adipiscing elit. Morbi sollicitudin convallis elementum. Nullam cursus condimentum lectus.</p>
    <p>Curabitur at mi a lectus feugiat cursus sed in est. Donec ac ipsum elit, vitae egestas augue.</p>
    <a class="read-more" href="#">Read more...</a>
  </article>
  <article class="feature">
    <div class="feature-head">
      <span class="feature-icon"><svg width="14" height="14" viewBox="0 0 14 14"><rect x="1" y="8" width="3" height="5" fill="#fff"/><rect x="5.5" y="5" width="3" height="8" fill="#fff"/><rect x="10" y="2" width="3" height="11" fill="#fff"/></svg></span>
      <span class="feature-title">Development</span>
    </div>
    <p class="lead">Lorem ipsum dolor sit amet, consectetur adipiscing elit. Morbi sollicitudin convallis elementum. Nullam cursus condimentum lectus.</p>
    <p>Curabitur at mi a lectus feugiat cursus sed in est. Donec ac ipsum elit, vitae egestas augue.</p>
    <a class="read-more" href="#">Read more...</a>
  </article>
  <article class="feature">
    <div class="feature-head">
      <span class="feature-icon"><svg width="14" height="14" viewBox="0 0 14 14"><path d="M2 12L12 2M6 2h6v6" fill="none" stroke="#fff" stroke-width="2"/></svg></span>
      <span class="feature-title">Kelvar Strategy</span>
    </div>
    <p class="lead">Lorem ipsum dolor sit amet, consectetur adipiscing elit. Morbi sollicitudin convallis elementum. Nullam cursus condimentum lectus.</p>
    <p>Curabitur at mi a lectus feugiat cursus sed in est. Donec ac ipsum elit, vitae egestas augue.</p>
    <a class="read-more" href="#">Read more...</a>
  </article>
</section>

<footer class="site-footer">
  <div class="footer-col col-links">
    <h3>Quick Links</h3>
    <ul>
      <li>Home</li><li>Our Company</li><li>Developments</li><li>Inspiration</li><li>Partners</li><li>Contact Us</li>
    </ul>
  </div>
  <div class="footer-col col-news">
    <h3>Latest News &amp; Events</h3>
    <p>Lorem ipsum dolor sit amet, consectetur adipiscing elit. Cras ut dolor nisl. Lorem ipsum dolor sit.</p>
    <p class="date">18 February, 2013</p>
    <p>Lorem ipsum dolor sit amet, consectetur adipiscing elit. Cras ut dolor nisl. Lorem ipsum dolor sit.</p>
    <p class="date">18 February, 2013</p>
  </div>
  <div class="footer-col col-signup">
    <h3>Newsletter Signup</h3>
    <p>Enter your Email here to get our newsletter in your inbox:</p>
    <div class="signup-input">Enter Your Email</div>
    <div class="signup-btn">Subscribe</div>
  </div>
  <div class="footer-col col-contact">
    <h3>Contact Us</h3>
    <ul>
      <li>Request A Call Back</li><li>Enquire Form</li><li>Request Free Info Pack</li>
    </ul>
    <div class="contact-brand">
      <span class="brand-mark"></span>
      <span class="brand-name">KELVAR BUILDS INC.</span>
    </div>
  </div>
  <div class="footer-rule"></div>
  <p class="copyright">Copyright 2012 Kelvar Builds | Privacy Policy | Disclaimer</p>
</footer>

</body>
</html>
```